Sacred Anointing Oils need new label

Beautiful sacred oils need a new label. There are 4 oils with 4 key colours. The labels need to match together, so they look good on a shop shelf. They have a feeling of warmth, simplicity, beauty, non religious, yet sacred. Engaging. I have now created a photoshop mockup of what I like and will attach the psd files.
I will attach the current cards to give you more of a feel of the oils. There is not a card yet for Halbrey. The cards will also need to be changed, as another project, once the labels are completed.

There are 4 Oils, Spikenard, Verolinde, Halbrey, Amber Hush. They each have matching cards to go with them. The labels go on 15ml cobalt blue glass bottles. The size is 85mm x 42mm including bleed. I need them laid out on an A4 sheet, I can fit 12 per page. Slightly rounded corners. Each bottle is the same layout, different colour scheme. Header font is Apple chancery.

Target Market(s)

Women 15-80

Industry/Entity Type

Shop

Contact Information for Business Card

Please see attached information and logo

Font styles to use
Other font styles liked:
• There will be simple san serif font for the contents details. the title name eg Verolinde can be more script or decorative. I have used QumpellikaNo12 in the past, and Apple Chancery. am open to similar options.

Requirements
Must have
• 4 labels are attached with the mockup design of what I want. Must be
• clear and easy to read, a feeling of warmth, rich colours. Must be one label per bottle (not two), rectangular wrapping around bottle. Not 2 labels per bottle. The label size must be 42mm height and a minimum of 88mm in length around bottle - this includes bleed. The actual height of the label, without bleed must be a maximum of 37mm and width 89mm max.
Nice to have
• The image from logo needs to be eye catching and drawing people in, a sense of flow.
Should not have
• Must not be clunky, hard to read, two labels. No religious imagery

```html
<!DOCTYPE html>
<html lang="en">
<head>
<meta charset="utf-8">
<title>Lumen Grove Anointing Oil Labels</title>
<link rel="stylesheet" href="https://fonts.googleapis.com/css2?family=Montserrat:wght@400;500;600&family=Oswald:wght@500;600&family=Courgette&display=swap">
<style>
  :root {
    --backdrop: #ececec;
    --paper: #ffffff;
    --brand-red: #6e1b1e;
    --band-red: #d8203f;
    --olive: #626331;
    --orange: #f08a2c;
    --violet-top: #6b55a6;
    --violet-bottom: #8a3388;
    --frame-deep: #3e2f6b;
    --frame-mid: #5a4390;
    --gold: #d9ad3c;
    --gold-light: #f3d77a;
    --white: #ffffff;
  }
  * { margin: 0; padding: 0; box-sizing: border-box; }
  html, body { width: 1200px; height: 1200px; overflow: hidden; }
  body {
    background: var(--backdrop);
    position: relative;
    font-family: "Montserrat", Arial, sans-serif;
  }
  .label {
    position: absolute;
    top: 516px;
    width: 228px;
    height: 352px;
    overflow: hidden;
  }
  .label--halbrey { left: 148px; background: var(--olive); }
  .label--spikenard { left: 485px; background: linear-gradient(180deg, var(--violet-top), var(--violet-bottom)); }
  .label--amber { left: 827px; background: linear-gradient(180deg, var(--violet-top) 0%, #7c45a0 45%, var(--violet-bottom) 100%); }

  .label__head {
    position: absolute; left: 0; top: 0; width: 100%; height: 150px;
    background: var(--paper);
  }
  .label--spikenard .label__head { height: 152px; }

  .brand {
    position: absolute; left: 0; width: 100%;
    text-align: center; color: var(--brand-red);
    font-family: "Montserrat", Arial, sans-serif; font-weight: 500;
    line-height: 1;
  }
  .brand__dot {
    position: absolute; left: 50%; width: 34px; height: 34px;
    margin-left: -17px; border-radius: 50%;
    background: var(--violet-bottom);
  }
  .brand__main { display: block; font-size: 27px; letter-spacing: 6px; padding-left: 6px; }
  .brand__sub { display: block; font-size: 16px; letter-spacing: 3px; padding-left: 3px; margin-top: 6px; }

  .label--halbrey .brand__dot { top: 30px; }
  .label--halbrey .brand { top: 90px; }
  .label--amber .brand__dot { top: 30px; background: var(--orange); }
  .label--amber .brand { top: 92px; color: #8a2c3c; }

  .range-band {
    position: absolute; left: 0; width: 100%; height: 24px;
    background: var(--band-red); color: var(--white);
    font-size: 15.5px; font-weight: 500; text-align: center; line-height: 24px;
    letter-spacing: -0.2px;
  }
  .label--halbrey .range-band { top: 150px; }
  .label--amber .range-band { top: 154px; }
  .label--spikenard .range-band { top: 152px; }

  .oil-name {
    position: absolute; left: 0; width: 100%; text-align: center;
    font-family: "Oswald", "Arial Narrow", sans-serif; font-weight: 600;
    color: var(--orange); line-height: 1;
  }
  .label--halbrey .oil-name { top: 196px; font-size: 44px; letter-spacing: 1px; }
  .label--amber .oil-name { top: 188px; font-size: 40px; letter-spacing: 0; }

  .weight {
    position: absolute; left: 0; width: 100%; text-align: center;
    font-size: 17px; letter-spacing: 1px;
  }
  .label--halbrey .weight { top: 318px; color: var(--orange); }
  .label--amber .weight { top: 322px; color: var(--white); }
  .label--spikenard .weight { top: 326px; color: var(--white); }

  .ornament {
    position: absolute; width: 40px; height: 80px; top: 10px;
    background: linear-gradient(160deg, var(--gold-light), var(--gold));
    opacity: 0.55; border-radius: 20px;
  }
  .ornament--left { left: 26px; }
  .ornament--right { right: 26px; }

  .frame {
    position: absolute; left: 27px; top: 36px; width: 174px; height: 250px;
    border: 4px solid var(--gold);
    border-radius: 26px;
    background: radial-gradient(ellipse at 50% 45%, var(--frame-mid), var(--frame-deep));
    box-shadow: 0 0 0 1px var(--gold-light) inset;
  }
  .frame .brand { top: 22px; color: #b02a4a; }
  .frame .brand__dot { position: relative; display: block; left: 0; margin: 0 auto 6px; width: 24px; height: 24px; background: var(--band-red); }
  .frame .brand__main { font-size: 17px; letter-spacing: 3px; padding-left: 3px; }
  .frame .brand__sub { font-size: 10px; letter-spacing: 1.5px; margin-top: 2px; }
  .frame__title {
    position: absolute; left: 0; top: 118px; width: 100%;
    text-align: center; color: var(--white);
    font-size: 25px; font-weight: 500; line-height: 38px; letter-spacing: -0.3px;
  }
  .ribbon {
    position: absolute; left: 28px; top: 284px; width: 172px; height: 34px;
    background: linear-gradient(180deg, #e0304d, #b81834);
    border: 2px solid var(--gold);
    border-radius: 4px;
    color: var(--white); text-align: center;
    font-family: "Courgette", "Brush Script MT", cursive;
    font-size: 22px; line-height: 30px;
    transform: rotate(-3deg);
  }
</style>
</head>
<body>

  <section class="label label--halbrey">
    <div class="label__head"></div>
    <span class="brand__dot"></span>
    <div class="brand"><span class="brand__main">LUMEN</span><span class="brand__sub">GROVE</span></div>
    <div class="range-band">SACRED ANOINTING OILS</div>
    <h2 class="oil-name">HALBREY</h2>
    <p class="weight">200g</p>
  </section>

  <section class="label label--spikenard">
    <div class="label__head"></div>
    <div class="range-band"></div>
    <div class="ornament ornament--left" role="img" aria-label="Gold scroll ornament"></div>
    <div class="ornament ornament--right" role="img" aria-label="Gold scroll ornament"></div>
    <div class="frame">
      <div class="brand"><span class="brand__dot"></span><span class="brand__main">LUMEN</span><span class="brand__sub">GROVE</span></div>
      <h2 class="frame__title">SACRED<br>ANOINTING<br>OILS</h2>
    </div>
    <div class="ribbon">Spikenard</div>
    <p class="weight">200g</p>
  </section>

  <section class="label label--amber">
    <span class="brand__dot"></span>
    <div class="brand"><span class="brand__main">LUMEN</span><span class="brand__sub">GROVE</span></div>
    <div class="range-band">SACRED ANOINTING OILS</div>
    <h2 class="oil-name">AMBER HUSH</h2>
    <p class="weight">200g</p>
  </section>

</body>
</html>
```